Design some Business Cards for The Larkspur

I require a design for business cards that is based off my current design theme.

I want them to be fun but professional.

Must use Timber/yellow background/cherry logo as attached and on website

The website is www.thelarkspur.com.au and the files needed are attached.

The text requires the following fields:

Graham Mulvey
Managing Director
Phone - XXXX XXX XXX
Email - graham@thelarkspur.com.au
www.thelarkspur.com.au

Full Bleed Size (starting document size)
90 x 52 mm
1062 x 615 pixels
* Finished artwork should use the full bleed dimensions

Document Trim Size (final size after being cut)
87 x 49 mm
1028 x 579 pixels
* Please be sure to keep all text within the safe margin.

Resolution
300 DPI

All designs must be provided in .PSD upon completion.

```html
<!DOCTYPE html>
<html lang="en">
<head>
<meta charset="utf-8">
<title>The Larkspur – Business Card</title>
<link href="https://fonts.googleapis.com/css2?family=Arimo:wght@400;700&display=swap" rel="stylesheet">
<style>
  :root {
    --stage: #1670c2;
    --yellow: #ffe23a;
    --yellow-pale: #f7e88a;
    --timber-light: #8a5a35;
    --timber-dark: #4e3019;
    --cherry-red: #d4161f;
    --cherry-deep: #8d0b10;
    --strip: rgba(20, 4, 4, 0.82);
    --ink: #111111;
    --white: #ffffff;
    --badge-ring: #f5c400;
  }
  * { box-sizing: border-box; margin: 0; padding: 0; }
  html, body {
    width: 1200px; height: 617px; overflow: hidden;
    background: var(--stage);
    font-family: "Arimo", Arial, sans-serif;
  }
  .business-card {
    position: absolute; left: 100px; top: 19px;
    width: 1000px; height: 578px;
    overflow: hidden;
    background: var(--yellow);
  }
  .band-top {
    position: absolute; left: 0; top: 0; width: 100%; height: 30px;
    background: var(--yellow);
  }
  .timber {
    position: absolute; left: 0; top: 30px; width: 100%; height: 500px;
    background: linear-gradient(90deg, var(--timber-dark), var(--timber-light) 25%, var(--timber-dark) 55%, var(--timber-light) 80%, var(--timber-dark));
  }
  .band-bottom {
    position: absolute; left: 0; top: 530px; width: 100%; height: 48px;
    background: linear-gradient(180deg, var(--yellow) 0 45%, var(--yellow-pale) 45% 100%);
  }
  .cherry-panel {
    position: absolute; left: 77px; top: 40px; width: 872px; height: 472px;
    background: radial-gradient(circle at 70% 45%, var(--cherry-red), var(--cherry-deep) 75%);
  }
  .fixing {
    position: absolute; width: 12px; height: 12px; border-radius: 50%;
    background: #2a1a12; border: 2px solid #9a8a80;
  }
  .badge {
    position: absolute; left: 18px; top: 38px;
    width: 410px; height: 410px; border-radius: 50%;
    background: var(--white);
    border: 12px solid var(--badge-ring);
    display: flex; align-items: center; justify-content: center;
    text-align: center;
  }
  .brand-name {
    font-weight: 700; font-size: 64px; line-height: 1.05;
    color: var(--ink); text-transform: uppercase; letter-spacing: -1px;
  }
  .contact-strip {
    position: absolute; left: 518px; top: 141px; width: 482px; height: 295px;
    background: var(--strip);
  }
  .contact {
    position: absolute; left: 548px; top: 160px; color: var(--white);
  }
  .person-name, .person-role {
    color: var(--yellow); font-weight: 700; font-size: 31px; line-height: 43px;
  }
  .contact-list { list-style: none; margin-top: 30px; }
  .contact-list li {
    display: flex; align-items: center; gap: 12px;
    font-size: 28px; height: 48px;
  }
  .contact-list .web { font-weight: 700; }
  .icon { width: 26px; height: 26px; flex: none; }
</style>
</head>
<body>
  <main class="business-card">
    <div class="band-top"></div>
    <div class="timber" role="img" aria-label="Timber plank texture background"></div>
    <div class="band-bottom"></div>
    <div class="cherry-panel" role="img" aria-label="Close-up photograph of fresh red cherries"></div>

    <span class="fixing" style="left:95px;top:58px"></span>
    <span class="fixing" style="left:920px;top:58px"></span>
    <span class="fixing" style="left:95px;top:486px"></span>
    <span class="fixing" style="left:920px;top:486px"></span>

    <div class="badge">
      <span class="brand-name">The<br>Larkspur</span>
    </div>

    <div class="contact-strip"></div>
    <section class="contact">
      <p class="person-name">Graham Mulvey</p>
      <p class="person-role">Managing Director</p>
      <ul class="contact-list">
        <li>
          <svg class="icon" viewBox="0 0 26 26" aria-hidden="true">
            <circle cx="13" cy="13" r="13" fill="var(--yellow)"/>
            <path d="M9 6.5c1 0 2.2 2.6 2.2 3.4 0 .8-1.3 1.2-1.1 2 .4 1.6 2.3 3.6 3.9 4 .8.2 1.2-1.1 2-1.1.8 0 3.4 1.2 3.4 2.2 0 1.4-1.6 2.5-3 2.5C11 19.5 6.5 15 6.5 9.5 6.5 8.1 7.6 6.5 9 6.5z" fill="#1a0a0a"/>
          </svg>
          <span>088-0047-0192</span>
        </li>
        <li>
          <svg class="icon" viewBox="0 0 26 26" aria-hidden="true">
            <rect x="1" y="5" width="24" height="16" fill="var(--yellow)"/>
            <path d="M1 5l12 9 12-9" fill="none" stroke="#1a0a0a" stroke-width="2"/>
          </svg>
          <span>graham@thelarkspur.com.au</span>
        </li>
        <li>
          <svg class="icon" viewBox="0 0 26 26" aria-hidden="true">
            <circle cx="13" cy="13" r="12" fill="var(--yellow)"/>
            <g fill="none" stroke="#1a0a0a" stroke-width="1.6">
              <circle cx="13" cy="13" r="8"/>
              <ellipse cx="13" cy="13" rx="3.5" ry="8"/>
              <path d="M5 13h16M6.5 9h13M6.5 17h13"/>
            </g>
          </svg>
          <span class="web">www.thelarkspur.com.au</span>
        </li>
      </ul>
    </section>
  </main>
</body>
</html>
```